Olive Oil 500ml bottle Lable

Dear Designer,

We would like you to design a high quality high class Olive Oil label for a 500ml Dark Round Bottle. (I have attached a image of the bottle)

The olive oil is a premium Australian Product so the design must reflect that. my requirements are all as follows

I have attached the master artwork files for a previous design and require you to submit a totally new design within the exact same size proportions. 190mmx66mm

The brand will be Marabel Ridge Olive Oil Gold and i have attached our Wine label so that you can use our brand logo.

I wish for the label to be color themed Gold foil printing on perhaps a red background i wish the label to be of abstract aboriginal art consisting of a olive tree and a Kangaroo and emu facing each other on either side of the tree as on the "Australian code of Arms". I wish the tree and the Kangaroo and Emu the be in gold abstract. and possibly a red background. i have attached some images to inspire design of olive trees, kangaroos and emus in the aboriginial abstract art i wish to reflect. i what the dots making up the picture all the be in gold.

The back label can be almost exactly the same except for the change of brand name and colour theme to much the front. The detail at bottom which will be changed to the text bellow.

Produced By: Blue Heron Trading
Address: Shop 4, 218 Upper Kessling Road Dunmore SA 5082
Website: www.blueherontrading.example
INGREDIENTS: 100% AUSTRALIAN EXTRA VIRGIN OLIVE OIL

please also leave the space for the bar code on the back label as is on the sample attached

Thank you and i look forward to the designs

Target Market(s)

Chinese Market
Expensive Gift

Requirements
Must have
• The same nutrition chart and descriptive text as on previous label (attached)
• Space for Barcode on rear lable
• The same product information as on sample (attached) eg Australian First Cold Pressed Olive Oil, 500ml 16.9 fl oz, 100% product of Australia, Extra Virgin Olive Oil
Nice to have
• Cheap real life images/Photos

```html
<!DOCTYPE html>
<html lang="en">
<head>
<meta charset="utf-8">
<title>Marabel Ridge Extra Virgin Olive Oil Gold – 500ml Label</title>
<link rel="stylesheet" href="https://fonts.googleapis.com/css2?family=Tinos:ital,wght@0,400;0,700;1,400&family=Arimo:wght@400;700&family=Cinzel:wght@700;900&display=swap">
<style>
  :root {
    --red-deep: #d8161b;
    --red: #ee2a1f;
    --orange: #f6821f;
    --orange-light: #fbb040;
    --gold: #f7d117;
    --gold-dark: #c58a12;
    --yellow: #ffe600;
    --white: #ffffff;
    --ink: #111111;
    --barcode-grey: #b6b6bc;
    --olive: #5f9a2a;
  }
  * { box-sizing: border-box; margin: 0; padding: 0; }
  html, body { width: 956px; height: 1200px; overflow: hidden; background: var(--white); }
  .canvas { position: relative; width: 956px; height: 1200px; background: var(--white); font-family: "Tinos", "Times New Roman", serif; color: var(--ink); }

  /* ---------- Back label ---------- */
  .back-label { position: absolute; left: 7px; top: 0; width: 414px; height: 697px;
    background: radial-gradient(ellipse at 50% 45%, var(--red) 0%, var(--red-deep) 60%, #f04a1d 100%); color: var(--white); }
  .back-label .brand { position: absolute; left: 0; right: 0; top: 48px; text-align: center;
    font-size: 58px; font-weight: 400; color: var(--white); letter-spacing: 1px; }
  .back-label .subtitle { position: absolute; left: 0; right: 0; top: 134px; text-align: center; font-size: 22px; }
  .back-label .subtitle .accent { color: var(--gold); }
  .back-label .intro { position: absolute; left: 22px; right: 18px; top: 215px; font-size: 21px; line-height: 1.28; }
  .claims { position: absolute; left: 22px; top: 455px; width: 370px; display: grid; grid-template-columns: 1fr 1fr; row-gap: 6px; column-gap: 12px; font-size: 11px; }
  .claims li { list-style: none; display: flex; align-items: center; gap: 6px; }
  .claims svg { width: 15px; height: 15px; flex: none; }
  .barcode-space { position: absolute; left: 22px; top: 543px; width: 360px; height: 70px; background: var(--barcode-grey); }
  .back-label .storage { position: absolute; left: 22px; top: 632px; font-size: 14.5px; line-height: 1.3; }

  /* Nutrition */
  .nutrition { position: absolute; left: 7px; top: 715px; width: 214px; font-family: "Arimo", Arial, sans-serif; font-size: 9.5px; border: 1.5px solid var(--ink); }
  .nutrition .serving { padding: 4px 6px; border-bottom: 1.5px solid var(--ink); line-height: 1.35; font-weight: 700; }
  .nutrition .serving span { display: block; text-align: center; }
  .nutrition table { width: 100%; border-collapse: collapse; }
  .nutrition th { font-size: 6.5px; font-weight: 700; text-align: center; padding: 2px; border-left: 1px solid var(--ink); border-bottom: 1.5px solid var(--ink); }
  .nutrition th:first-child { border-left: 0; }
  .nutrition td { padding: 0 6px; line-height: 1.2; }
  .nutrition td + td { text-align: center; border-left: 1px solid var(--ink); padding: 0 2px; }
  .nutrition tr.gap td { padding-top: 8px; }
  .nutrition .foot { border-top: 1.5px solid var(--ink); text-align: center; font-size: 8px; padding: 3px 4px; line-height: 1.25; }
  .nutrition .foot b { font-size: 9px; }
  .origin { position: absolute; left: 243px; top: 735px; font-family: "Arimo", Arial, sans-serif; font-weight: 700; font-size: 20px; line-height: 1.15; }
  .origin .volume { margin-top: 6px; font-weight: 400; font-size: 13px; display: flex; gap: 38px; }

  .producer { position: absolute; left: 7px; top: 1022px; width: 420px; font-family: "Arimo", Arial, sans-serif; font-size: 16px; line-height: 1.3; }
  .producer dl { display: grid; grid-template-columns: 114px 1fr; row-gap: 8px; }
  .producer dt { font-weight: 700; }
  .producer .ingredients { margin-top: 22px; font-size: 13px; }

  /* ---------- Front label ---------- */
  .front-label { position: absolute; left: 544px; top: 0; width: 403px; height: 1200px;
    background: radial-gradient(ellipse at 50% 55%, var(--red-deep) 0%, var(--red) 45%, var(--orange) 100%);
    border: 3px solid var(--orange-light); color: var(--white); }
  .front-label .olive-photo { position: absolute; left: 30px; top: 0; width: 342px; height: 210px;
    background: radial-gradient(ellipse at 40% 65%, #8fbf3a 0%, var(--olive) 45%, #e9e4cf 80%, #f5f1e4 100%); }
  .front-label .brand { position: absolute; left: 0; right: 0; top: 232px; text-align: center; font-size: 56px; color: var(--white); }
  .front-label .emblem { position: absolute; left: 50px; top: 312px; width: 300px; height: 300px;
    background: radial-gradient(circle at 50% 50%, var(--gold) 0%, var(--gold-dark) 45%, rgba(216,22,27,0) 72%); }
  .front-label .first { position: absolute; left: 0; right: 0; top: 632px; text-align: center; font-weight: 700; font-size: 31px; line-height: 1.2; color: var(--white); }
  .front-label .title { position: absolute; left: 0; right: 0; text-align: center; font-family: "Cinzel", "Times New Roman", serif; font-weight: 900; line-height: 1; letter-spacing: 3px; }
  .title.extra-virgin { top: 735px; font-size: 58px; color: var(--red-deep); -webkit-text-stroke: 1.5px var(--gold); }
  .title.olive-oil { top: 862px; font-size: 52px; color: var(--yellow); -webkit-text-stroke: 1px var(--gold-dark); }
  .title.gold { top: 985px; font-size: 58px; color: var(--gold); -webkit-text-stroke: 1px var(--gold-dark); letter-spacing: 6px; }
  .front-label .volume-band { position: absolute; left: 0; right: 0; top: 1085px; height: 100px;
    background: linear-gradient(var(--orange-light), var(--orange)); text-align: center; font-weight: 700; color: var(--white); }
  .volume-band .volume { display: flex; justify-content: center; gap: 60px; font-size: 27px; padding-top: 16px; }
  .volume-band .country { font-size: 22px; margin-top: 8px; }
</style>
</head>
<body>
<main class="canvas">

  <section class="back-label" aria-label="Back label">
    <h2 class="brand">Marabel Ridge</h2>
    <p class="subtitle">Extra Virgin <span class="accent">OLIVE OIL</span></p>
    <p class="intro">Marabel Ridge Olive Oil is made from fresh olive varieties cold pressed within 24 hours of harvest. This process ensures the oil delivers maximum health benefits including antioxidants and wonderful flavour that can be enjoyed naturally on fresh food or on its own.</p>
    <ul class="claims">
      <li><svg viewBox="0 0 15 15"><rect x="0.75" y="0.75" width="13.5" height="13.5" fill="none" stroke="#fff" stroke-width="1.5"/><path d="M3 8l3 3 6-7" fill="none" stroke="#fff" stroke-width="1.6"/></svg>No GMO</li>
      <li><svg viewBox="0 0 15 15"><rect x="0.75" y="0.75" width="13.5" height="13.5" fill="none" stroke="#fff" stroke-width="1.5"/><path d="M3 8l3 3 6-7" fill="none" stroke="#fff" stroke-width="1.6"/></svg>No Preservative</li>
      <li><svg viewBox="0 0 15 15"><rect x="0.75" y="0.75" width="13.5" height="13.5" fill="none" stroke="#fff" stroke-width="1.5"/><path d="M3 8l3 3 6-7" fill="none" stroke="#fff" stroke-width="1.6"/></svg>No Additives</li>
      <li><svg viewBox="0 0 15 15"><rect x="0.75" y="0.75" width="13.5" height="13.5" fill="none" stroke="#fff" stroke-width="1.5"/><path d="M3 8l3 3 6-7" fill="none" stroke="#fff" stroke-width="1.6"/></svg>100% Australian grown</li>
      <li><svg viewBox="0 0 15 15"><rect x="0.75" y="0.75" width="13.5" height="13.5" fill="none" stroke="#fff" stroke-width="1.5"/><path d="M3 8l3 3 6-7" fill="none" stroke="#fff" stroke-width="1.6"/></svg>100% Natural Product</li>
      <li><svg viewBox="0 0 15 15"><rect x="0.75" y="0.75" width="13.5" height="13.5" fill="none" stroke="#fff" stroke-width="1.5"/><path d="M3 8l3 3 6-7" fill="none" stroke="#fff" stroke-width="1.6"/></svg>Natural Source of Antioxidants</li>
    </ul>
    <div class="barcode-space" aria-label="Barcode space"></div>
    <p class="storage">Store away from direct sunlight at room temperature<br>NUTRITION INFORMATION</p>
  </section>

  <section class="nutrition" aria-label="Nutrition information">
    <p class="serving"><span>SERVING PER PACKAGE: 33.33</span><span>Serving Size: 15ml / 3 tsps</span></p>
    <table>
      <tr><th></th><th>QUANTITY PER SERVING</th><th>QUANTITY 100ml</th></tr>
      <tr class="gap"><td>ENERGY kj (cal)</td><td>517kj</td><td>3447kj</td></tr>
      <tr><td>PROTEIN</td><td>0.0g</td><td>0.0g</td></tr>
      <tr><td>FAT - TOTAL</td><td>13.7g</td><td>91.7g</td></tr>
      <tr><td>- Saturated Fat</td><td>1.8g</td><td>13.9g</td></tr>
      <tr><td>- TRANS</td><td>&lt;0.01g</td><td>&lt;0.05g</td></tr>
      <tr><td>- Polyunsaturated</td><td>1.5g</td><td>9.9g</td></tr>
      <tr><td>- Monounsaturated</td><td>10.2g</td><td>67.9g</td></tr>
      <tr class="gap"><td>CHOLESTROL</td><td>0.0g</td><td>0.0g</td></tr>
      <tr><td>CARBOHYDRATE</td><td>0.0g</td><td>0.0g</td></tr>
      <tr><td>- TOTAL</td><td>0.0g</td><td>0.0g</td></tr>
      <tr><td>- SUGARS</td><td>0.0g</td><td>0.0g</td></tr>
      <tr><td>SODIUM mg (mmol)</td><td>0.0g</td><td>0.0g</td></tr>
    </table>
    <p class="foot">Total Acidity as Oleic Acid Less Than <b>0.5%</b><br><b>NOTE:</b> All values are considered averages unless otherwise indicated</p>
  </section>

  <div class="origin">100%<br>AUSTRALIAN<br>PRODUCT
    <div class="volume"><span>500ml</span><span>16.9fl oz</span></div>
  </div>

  <section class="producer" aria-label="Producer details">
    <dl>
      <dt>Produced by :</dt><dd>Blue Heron Trading</dd>
      <dt>Address:</dt><dd>Shop 4, 218 Upper Kessling Road,<br>Dunmore SA 5082</dd>
      <dt>Website :</dt><dd>www.blueherontrading.example</dd>
    </dl>
    <p class="ingredients"><b>INGREDIENTS :</b> 100% AUSTRALIAN EXTRA VIRGIN OLIVE OIL</p>
  </section>

  <section class="front-label" aria-label="Front label">
    <div class="olive-photo" role="img" aria-label="Photograph of a dish of olive oil with green olives and olive leaves"></div>
    <h1 class="brand">Marabel Ridge</h1>
    <div class="emblem" role="img" aria-label="Gold dot-art illustration of an olive tree with a kangaroo and an emu facing each other"></div>
    <p class="first">Australian First<br>Cold Pressed</p>
    <p class="title extra-virgin">EXTRA<br>VIRGIN</p>
    <p class="title olive-oil">OLIVE<br>OIL</p>
    <p class="title gold">GOLD</p>
    <div class="volume-band">
      <p class="volume"><span>500ml</span><span>16.9 fl oz</span></p>
      <p class="country">100% PRODUCT OF AUSTRALIA</p>
    </div>
  </section>

</main>
</body>
</html>
```